Business Card for Professional Photographer

I'm looking for an eye catching modern clean design that compliments my logo/ website fonts & colours.
I specialise in architecture, corporate & commercial photography so I'm marketing to professional clients rather than portrait / wedding clients.

I would prefer to not have a solid black design.

My logo brand guide is as follows :

Main front font. : Reislust
Main font colour : #fff
Slogan front font : Ubuntu Bold
Monogram front font : Venti Medium
Container colour : #fff

I need print ready files in pdf .png & .eps formats.

Included in the files below are some screen grabs as reference to font & colours etc.

```html
<!DOCTYPE html>
<html lang="en">
<head>
<meta charset="utf-8">
<title>Northlight Studio – Business Card</title>
<link href="https://fonts.googleapis.com/css2?family=Ubuntu:wght@400;500;700&display=swap" rel="stylesheet">
<style>
  :root {
    --bg: #e4e4e4;
    --card: #cc9c5c;
    --ink: #ffffff;
  }
  * { margin: 0; padding: 0; box-sizing: border-box; }
  html, body {
    width: 1200px; height: 1200px; overflow: hidden;
    background: var(--bg);
    font-family: "Ubuntu", sans-serif;
    color: var(--ink);
  }
  .canvas { position: relative; width: 1200px; height: 1200px; }
  .card { position: absolute; left: 392px; width: 416px; height: 353px; }
  .card--front { top: 184px; }
  .card--back { top: 672px; }
  .card-shape { position: absolute; inset: 0; width: 416px; height: 353px; }
  .card-shape path { fill: var(--card); }
  .card-content { position: absolute; left: 0; right: 0; text-align: center; }
  .front-info { top: 94px; }
  .holder-name { font-size: 23px; font-weight: 700; letter-spacing: 0.3px; line-height: 26px; }
  .holder-title { font-size: 16px; font-weight: 500; line-height: 20px; }
  .divider { font-size: 13px; line-height: 14px; letter-spacing: 0.5px; margin: 0 0 6px; }
  .address { font-size: 15px; line-height: 19px; margin-bottom: 2px; }
  .contact { font-size: 15.5px; line-height: 21px; }
  .brand {
    top: 164px; display: flex; justify-content: center; align-items: center; gap: 14px;
  }
  .brand-mark { width: 36px; height: 36px; background: var(--ink); }
  .brand-name { font-size: 26px; font-weight: 500; line-height: 30px; }
</style>
</head>
<body>
<main class="canvas">
  <section class="card card--front">
    <svg class="card-shape" viewBox="0 0 416 353" aria-hidden="true">
      <path d="M0 104 A55 55 0 0 1 55 49 L79 49 A12 12 0 0 0 91 37 L91 36 A36 36 0 0 1 127 0 L289 0 A36 36 0 0 1 325 36 L325 37 A12 12 0 0 0 337 49 L361 49 A55 55 0 0 1 416 104 L416 298 A55 55 0 0 1 361 353 L55 353 A55 55 0 0 1 0 298 Z"/>
    </svg>
    <div class="card-content front-info">
      <h1 class="holder-name">DANIEL HART</h1>
      <p class="holder-title">PRESIDENT</p>
      <p class="divider">...................</p>
      <p class="address">4219 Willow Creek Lane<br>Fairbanks, Alaska 99701</p>
      <p class="divider">...................</p>
      <p class="contact">555-214-7730 | info@northlightstudio.com<br>www.northlightstudio.com</p>
    </div>
  </section>

  <section class="card card--back">
    <svg class="card-shape" viewBox="0 0 416 353" aria-hidden="true">
      <path d="M0 104 A55 55 0 0 1 55 49 L79 49 A12 12 0 0 0 91 37 L91 36 A36 36 0 0 1 127 0 L289 0 A36 36 0 0 1 325 36 L325 37 A12 12 0 0 0 337 49 L361 49 A55 55 0 0 1 416 104 L416 298 A55 55 0 0 1 361 353 L55 353 A55 55 0 0 1 0 298 Z"/>
    </svg>
    <div class="card-content brand">
      <span class="brand-mark" aria-hidden="true"></span>
      <p class="brand-name">Northlight Studio</p>
    </div>
  </section>
</main>
</body>
</html>
```